new marketing company logo and business card

design logo and biz card for marketing start up.

My company name needs a brand logo designed: Copper Lantern Marketing Co.
Tagline: Sales - Marketing - Brand Building

Sister Bay is the name of my favorite place, in Wisconsin, but the business is NOT BASED there. It should evoke warmth, friendliness, professionalism, and marketing services from a seasoned marketer.

Target Market(s)

I am selling my services to small business that need help.

Industry/Entity Type

Marketing

Contact Information for Business Card

Copper Lantern Marketing Co. (logo)
Sales - Marketing - Brand Building (tagline)

Dana M. Whitcombe
DanaMWhitcombe@fernlymail.com
555-384-0192 mobile

Font styles to use
Serif
Sans Serif

Colors
f78f20
f37122
f68d4d
00a990
85cae6
33b8a4
faa54b

Requirements
Must have
• a logo
• a business card
Nice to have
• I'd love to see a small subtle reference to Sister Bay built in. Sister bay is named that because there are two islands called ‘sister islands’ that flank the bay. If you google this you will see.
• I like warm, earthy colors. But, I am a fun, approachable, real person. Not stand-offish. Should be warm and appealing yet professional.
Should not have
• nothing cartoon-ish. no child-like fonts. this is a professional business.

```html
<!DOCTYPE html>
<html lang="en">
<head>
<meta charset="utf-8">
<title>Copper Lantern Marketing Co. — Business Card</title>
<link rel="stylesheet" href="https://fonts.googleapis.com/css2?family=Montserrat:wght@400;600;700&display=swap">
<style>
  :root {
    --page-bg: #e9e4de;
    --leaf-red: #b8231a;
    --leaf-deep: #8e1a12;
    --leaf-orange: #e5631c;
    --leaf-yellow: #f2b326;
    --leaf-green: #9a9a2c;
    --panel-orange: #f37122;
    --panel-light: #f78f20;
    --text-white: #ffffff;
    --text-soft: #ffe2c6;
    --rule: rgba(255, 236, 214, 0.85);
  }
  * { box-sizing: border-box; margin: 0; padding: 0; }
  html, body {
    width: 1200px;
    height: 809px;
    overflow: hidden;
    background: var(--page-bg);
    font-family: "Montserrat", Arial, sans-serif;
  }
  .card {
    position: absolute;
    left: 75px;
    top: 104px;
    width: 1050px;
    height: 600px;
    overflow: hidden;
    box-shadow: 0 10px 30px rgba(60, 40, 20, 0.25);
  }
  .card__foliage {
    position: absolute;
    inset: 0;
    background:
      radial-gradient(circle at 8% 12%, var(--leaf-yellow) 0 6%, transparent 16%),
      radial-gradient(circle at 92% 10%, var(--leaf-yellow) 0 5%, transparent 15%),
      radial-gradient(circle at 88% 88%, var(--leaf-yellow) 0 8%, transparent 18%),
      radial-gradient(circle at 45% 96%, var(--leaf-green) 0 8%, transparent 20%),
      radial-gradient(circle at 20% 90%, var(--leaf-deep) 0 6%, transparent 16%),
      radial-gradient(circle at 60% 6%, var(--leaf-deep) 0 6%, transparent 16%),
      linear-gradient(135deg, var(--leaf-red), var(--leaf-orange) 45%, var(--leaf-red) 75%, var(--leaf-orange));
  }
  .card__frame {
    position: absolute;
    left: 48px;
    top: 60px;
    right: 48px;
    bottom: 90px;
    border: 2px solid var(--rule);
  }
  .card__panel {
    position: absolute;
    left: 58px;
    top: 70px;
    right: 58px;
    bottom: 100px;
    background: linear-gradient(160deg, var(--panel-light), var(--panel-orange));
    opacity: 0.93;
  }
  .card__name {
    position: absolute;
    right: 100px;
    top: 102px;
    color: var(--text-white);
    font-weight: 700;
    font-size: 31px;
    letter-spacing: 0.5px;
  }
  .brand {
    position: absolute;
    left: 110px;
    top: 300px;
    color: var(--text-white);
  }
  .brand__name {
    font-weight: 700;
    font-size: 22px;
    letter-spacing: 0.5px;
    text-transform: uppercase;
    white-space: nowrap;
  }
  .brand__tagline {
    margin-top: 8px;
    font-weight: 400;
    font-size: 15px;
    letter-spacing: 1px;
    text-transform: uppercase;
    color: var(--text-soft);
    white-space: nowrap;
  }
  .card__divider {
    position: absolute;
    left: 585px;
    top: 248px;
    width: 2px;
    height: 150px;
    background: var(--rule);
  }
  .contact {
    position: absolute;
    left: 618px;
    top: 274px;
    list-style: none;
    color: var(--text-white);
    font-size: 16px;
    font-weight: 400;
  }
  .contact__item {
    display: flex;
    align-items: center;
    gap: 12px;
    margin-bottom: 18px;
    white-space: nowrap;
  }
  .contact__icon { width: 16px; height: 16px; flex: none; }
</style>
</head>
<body>
  <main class="card">
    <div class="card__foliage" role="img" aria-label="Photograph of red, orange, yellow and green autumn maple leaves covering the card"></div>
    <div class="card__frame"></div>
    <div class="card__panel"></div>

    <h1 class="card__name">Dana M. Whitcombe</h1>

    <div class="brand">
      <p class="brand__name">Copper Lantern Marketing Co</p>
      <p class="brand__tagline">Sales - Marketing - Brand Building</p>
    </div>

    <div class="card__divider"></div>

    <ul class="contact">
      <li class="contact__item">
        <svg class="contact__icon" viewBox="0 0 24 24" aria-hidden="true">
          <path fill="#ffffff" d="M6.6 10.8a15.1 15.1 0 0 0 6.6 6.6l2.2-2.2a1 1 0 0 1 1-.25 11.4 11.4 0 0 0 3.6.57 1 1 0 0 1 1 1V20a1 1 0 0 1-1 1A17 17 0 0 1 3 4a1 1 0 0 1 1-1h3.5a1 1 0 0 1 1 1c0 1.25.2 2.45.57 3.57a1 1 0 0 1-.25 1z"/>
        </svg>
        <span>555-384-0192</span>
      </li>
      <li class="contact__item">
        <svg class="contact__icon" viewBox="0 0 24 24" aria-hidden="true">
          <path fill="#ffffff" d="M2 5h20v14H2z"/>
          <path fill="none" stroke="#f37122" stroke-width="1.8" d="M2.5 5.5l9.5 7 9.5-7"/>
        </svg>
        <span>DanaMWhitcombe@fernlymail.com</span>
      </li>
    </ul>
  </main>
</body>
</html>
```